" Trabalhamos com café, bebidas a base de café, frapuccino, sorvetes, milk-shakes, taças, bolos, tortas doces e salgadas, doces, salgados assados e sucos. "

```html
<!DOCTYPE html>
<html lang="pt-BR">
<head>
<meta charset="UTF-8">
<title>Vellora — Banner Cafeteria</title>
<link href="https://fonts.googleapis.com/css2?family=Roboto+Condensed:wght@400;700&display=swap" rel="stylesheet">
<style>
  :root{
    --page:#ffffff;
    --panel:#2a150c;
    --panel-deep:#1e0e07;
    --tan:#e9c9a0;
    --gold:#f0a640;
    --cream:#f6ead8;
    --white:#ffffff;
    --muted:#cdbfb2;
  }
  *{margin:0;padding:0;box-sizing:border-box}
  html,body{width:1200px;height:1200px;overflow:hidden;background:var(--page)}
  .canvas{position:relative;width:1200px;height:1200px;background:var(--page)}
  .banner{position:absolute;left:0;top:377px;width:1200px;height:444px;overflow:hidden;background:var(--panel)}
  .banner__photo{position:absolute;left:420px;top:0;width:780px;height:444px;
    background:
      radial-gradient(ellipse 200px 150px at 560px 240px, #e9dccb 0%, #cdb59a 45%, rgba(0,0,0,0) 75%),
      radial-gradient(ellipse 210px 120px at 200px 150px, #c07a3a 0%, #8d4a1d 55%, rgba(0,0,0,0) 85%),
      linear-gradient(180deg,#3a2013 0%,#4a2814 45%,#2d180c 100%);}
  .banner__pattern{position:absolute;left:0;top:0;width:430px;height:444px;
    background:linear-gradient(135deg,var(--panel) 0%,var(--panel-deep) 100%)}
  .banner__stripe{position:absolute;left:0;top:0;width:1200px;height:444px}
  .menu{position:absolute;left:34px;top:32px;list-style:none;
    font-family:"Roboto Condensed",Arial Narrow,sans-serif;font-weight:700;
    font-size:26px;line-height:37.5px;color:var(--white)}
  .hours{position:absolute;left:34px;top:360px;display:flex;align-items:center;gap:12px;
    font-family:"Roboto Condensed",Arial Narrow,sans-serif;font-size:17px;line-height:19px}
  .hours__days{color:var(--muted)}
  .hours__time{color:var(--gold);font-weight:700}
  .brand{position:absolute;left:314px;top:81px;width:250px;height:250px;border-radius:50%;
    background:var(--panel);border:6px solid var(--cream);
    display:flex;align-items:center;justify-content:center}
  .brand__name{font-family:"Roboto Condensed",Arial Narrow,sans-serif;font-weight:700;
    font-size:44px;letter-spacing:3px;color:var(--cream)}
</style>
</head>
<body>
<div class="canvas">
  <section class="banner">
    <div class="banner__photo" role="img" aria-label="Foto de croissants açucarados e xícara de cappuccino sobre grãos de café"></div>
    <div class="banner__pattern" role="img" aria-label="Padrão ornamental marrom escuro"></div>
    <svg class="banner__stripe" viewBox="0 0 1200 444" aria-hidden="true">
      <polygon points="425,0 476,0 534,444 483,444" fill="var(--tan)"/>
    </svg>

    <ul class="menu">
      <li>Café Expresso</li>
      <li>Café Gourmet</li>
      <li>Frapuccino</li>
      <li>Sorvetes</li>
      <li>Taças</li>
      <li>Bolos</li>
      <li>Tortas Doces e Salgadas</li>
      <li>Assados</li>
      <li>Sucos Naturais</li>
    </ul>

    <div class="hours">
      <svg width="38" height="38" viewBox="0 0 38 38" aria-hidden="true">
        <circle cx="19" cy="19" r="18" fill="var(--gold)"/>
        <circle cx="19" cy="19" r="12" fill="none" stroke="var(--panel)" stroke-width="2.5"/>
        <path d="M19 11v8l5 4" fill="none" stroke="var(--panel)" stroke-width="2.5" stroke-linecap="round"/>
      </svg>
      <div>
        <div class="hours__days">De seg à Sáb</div>
        <div class="hours__time">das 08h às 17h</div>
      </div>
    </div>

    <div class="brand"><span class="brand__name">VELLORA</span></div>
  </section>
</div>
</body>
</html>
```